Winery needs to update tired, conservative wine label

We are a winery based in the Clare Valley of South Australia. We are looking to give an old, tired wine label a modern update to use particularly on Rose, but also across other vatieties including Riesling, Shiraz and Cabernet. The label could utilise parts of the old logo (horse shoe, grapes, leaves) but in a fresh modern way. Old artwork has been uploaded to show label as it currently is. We are looking for a label that pays tribute to the history of the brand (Colin Thorne: established 1977) but gives it a fresh, clean appearance that will be attractive to young professionals.

Target Market(s)

Male and Female young professionals, particularly Rose drinkers.

Font styles to use
Serif
Sans Serif

Colors

Designer to choose colors to be used in the design.

Requirements
Must have
• It must use the name Colin Thorne on the label, show region, vintage and variety. The label must work on a number of different wine bottle shapes and glass colours

```html
<!DOCTYPE html>
<html lang="en">
<head>
<meta charset="utf-8">
<title>Colin Thorne – Pinot Noir Rose Label</title>
<link rel="stylesheet" href="https://fonts.googleapis.com/css2?family=Cinzel:wght@400;500&family=Cormorant+Garamond:wght@400;500&display=swap">
<style>
  :root {
    --page: #ededed;
    --paper: #f8f8f7;
    --paper-edge: #f1f1f0;
    --night: #1e1e1e;
    --night-deep: #161616;
    --gold: #c29a3e;
    --gold-soft: #a8883f;
    --frame-white: #f4f4f4;
    --vintage-grey: #5a5a5a;
    --grape-grey: #4a4a4a;
  }
  * { box-sizing: border-box; margin: 0; padding: 0; }
  html, body { width: 1200px; height: 946px; overflow: hidden; }
  body { background: var(--page); position: relative; }

  .label {
    position: absolute; left: 100px; top: 75px;
    width: 1000px; height: 796px;
    background: var(--night);
    box-shadow: 0 4px 14px rgba(0,0,0,.25);
    overflow: hidden;
  }
  .label__top {
    position: absolute; left: 0; top: 0; width: 100%; height: 402px;
    background: linear-gradient(135deg, var(--paper-edge), var(--paper) 40%, #ffffff);
  }
  .label__bottom {
    position: absolute; left: 0; top: 402px; width: 100%; height: 394px;
    background: radial-gradient(ellipse at 50% 40%, #262626, var(--night-deep));
  }

  .brand-mark {
    position: absolute; left: 0; top: 92px; width: 100%;
    display: flex; justify-content: center; align-items: center; gap: 14px;
    font-family: "Cinzel", serif; font-weight: 400; font-size: 38px;
    color: var(--gold); letter-spacing: .08em;
  }
  .brand-mark__dot { width: 18px; height: 18px; border-radius: 50%; background: var(--gold); }

  .established {
    position: absolute; left: 0; top: 212px; width: 100%; text-align: center;
    font-family: "Cormorant Garamond", serif; font-size: 17px;
    letter-spacing: .5em; color: var(--gold-soft);
    font-variant-numeric: lining-nums;
  }

  .frame-bracket {
    position: absolute; left: 237px; top: 251px; width: 527px; height: 32px;
    border: 2px solid var(--gold); border-bottom: none;
  }

  .ornament {
    position: absolute; left: 480px; width: 40px; height: 5px;
    border-radius: 3px; background: var(--gold); opacity: .8;
  }
  .ornament--upper { top: 272px; }
  .ornament--lower { top: 660px; }

  .winery-name {
    position: absolute; left: 0; top: 298px; width: 100%; text-align: center;
    font-family: "Cinzel", serif; font-weight: 500; font-size: 90px;
    line-height: 1; color: var(--gold); white-space: nowrap;
  }

  .gold-band {
    position: absolute; top: 402px; height: 17px; background: var(--gold);
  }
  .gold-band--left { left: 0; width: 239px; }
  .gold-band--right { left: 762px; width: 238px; }

  .vintage-box {
    position: absolute; left: 237px; top: 402px; width: 527px; height: 209px;
    border: 2px solid var(--frame-white); border-top: none;
    background: rgba(0,0,0,.25);
  }
  .region {
    position: absolute; left: 0; top: 40px; width: 100%; text-align: center;
    font-family: "Cinzel", serif; font-size: 34px; letter-spacing: .3em;
    color: var(--gold); padding-left: .3em;
  }
  .vintage {
    position: absolute; left: 0; top: 108px; width: 100%; text-align: center;
    font-family: "Cormorant Garamond", serif; font-weight: 500; font-size: 108px;
    line-height: .75; color: var(--vintage-grey);
    font-variant-numeric: lining-nums;
  }

  .variety {
    position: absolute; left: 0; top: 700px; width: 100%; text-align: center;
    font-family: "Cinzel", serif; font-size: 48px; letter-spacing: .02em;
    color: var(--gold);
  }

  .grape-decoration {
    position: absolute; left: 770px; top: 442px; width: 230px; height: 276px;
    background: radial-gradient(ellipse at 55% 40%, var(--grape-grey), transparent 70%);
    opacity: .8;
  }
</style>
</head>
<body>
  <main class="label">
    <div class="label__top"></div>
    <div class="label__bottom"></div>

    <div class="brand-mark">
      <span class="brand-mark__dot"></span>
      <span class="brand-mark__name">Colin Thorne</span>
    </div>
    <p class="established">ESTD. 1977</p>

    <div class="frame-bracket"></div>
    <div class="ornament ornament--upper" role="img" aria-label="Small gold flourish ornament"></div>
    <h1 class="winery-name">COLIN THORNE</h1>

    <div class="gold-band gold-band--left"></div>
    <div class="gold-band gold-band--right"></div>

    <div class="grape-decoration" role="img" aria-label="Faint grey grape cluster decoration"></div>

    <section class="vintage-box">
      <p class="region">ADELAIDE HILLS</p>
      <p class="vintage">2017</p>
    </section>

    <div class="ornament ornament--lower" role="img" aria-label="Small gold flourish ornament"></div>
    <p class="variety">PINOT NOIR ROSE</p>
  </main>
</body>
</html>
```